Email Signature Gif Animation Design

We are looking for an interactive Email Signature to Standardize around for our growing company.

We are a commerical electrical contractor based out of North Jersey. We have a big corporate client tele and perfer a more professional fresh looking signature with titles and perhaps a suttle animation for effect.

Attached below is our company logo which is to be used prominently in the emai signature. We would consider a "refresh' of our logo design provided it does deviate too much.

We would like the tag Line "The KALV Electric Way" worked into that signature as a option.
Updates

Reviewing designs and am underwhelmed with the creativiity and designs, this is anyones prize!

Target Market(s)

Corporate / Middle Managers

Industry/Entity Type

Electrical Contracting & Engineering

Colors
FFF300
FFF600
FEFA6F
FFFEC7
FFFEE8

Requirements
Must have
• Must have, First & Last Name of Employee, Title of Employee, Office & Cell Phone Number, Email Address
Nice to have
• Gif Animation

```html
<!DOCTYPE html>
<html lang="en">
<head>
<meta charset="utf-8">
<title>Jordan Hale – KALV Electric Email Signature</title>
<link href="https://fonts.googleapis.com/css2?family=Oswald:wght@600&family=Open+Sans:ital,wght@0,400;0,600;1,400&display=swap" rel="stylesheet">
<style>
  :root {
    --gold: #cda51d;
    --ink: #111111;
    --paper: #ffffff;
    --dot-grey: #d9d9d9;
    --rule-grey: #c8c8c8;
  }
  html, body {
    margin: 0;
    padding: 0;
    overflow: hidden;
    background: var(--paper);
  }
  .signature {
    position: relative;
    width: 1200px;
    height: 323px;
    overflow: hidden;
    background: var(--paper);
    font-family: "Open Sans", Arial, sans-serif;
    color: var(--ink);
  }
  .halftone-corner {
    position: absolute;
    left: 0;
    top: 0;
    width: 380px;
    height: 310px;
    background: radial-gradient(ellipse at 0% 0%, var(--dot-grey) 0%, rgba(217,217,217,0.5) 40%, rgba(255,255,255,0) 75%);
  }
  .frame-shapes {
    position: absolute;
    inset: 0;
  }
  .company-mark {
    position: absolute;
    left: 336px;
    top: 58px;
    display: flex;
    align-items: center;
    gap: 10px;
    font-family: "Oswald", "Arial Narrow", sans-serif;
    font-weight: 600;
    font-size: 20px;
    letter-spacing: 0.06em;
    text-transform: uppercase;
    color: var(--ink);
  }
  .company-mark-square {
    width: 14px;
    height: 14px;
    background: var(--gold);
  }
  .company-tagline {
    position: absolute;
    right: 40px;
    top: 14px;
    margin: 0;
    font-style: italic;
    font-weight: 600;
    font-size: 18px;
    color: var(--ink);
  }
  .identity {
    position: absolute;
    left: 336px;
    top: 118px;
  }
  .person-name {
    margin: 0;
    font-family: "Oswald", "Arial Narrow", sans-serif;
    font-weight: 600;
    font-size: 54px;
    line-height: 1;
    letter-spacing: 0.05em;
    text-transform: uppercase;
    white-space: nowrap;
  }
  .person-title {
    margin: 16px 0 0;
    font-style: italic;
    font-size: 22px;
  }
  .divider {
    position: absolute;
    left: 709px;
    top: 100px;
    width: 4px;
    height: 156px;
    background: var(--gold);
  }
  .contacts {
    position: absolute;
    left: 742px;
    top: 102px;
    margin: 0;
    padding: 0;
    list-style: none;
  }
  .contact {
    display: flex;
    align-items: flex-start;
    margin-bottom: 12px;
    font-size: 22px;
    line-height: 37px;
  }
  .contact-icon {
    width: 34px;
    height: 34px;
    margin-right: 20px;
    flex: none;
  }
  .phone-lines {
    line-height: 29px;
    padding-top: 2px;
  }
  .phone-label {
    font-size: 10px;
    font-style: italic;
  }
  .social-links {
    position: absolute;
    left: 64px;
    top: 299px;
    display: flex;
    gap: 18px;
    font-size: 13px;
    color: var(--paper);
    line-height: 22px;
  }
</style>
</head>
<body>
<div class="signature">
  <div class="halftone-corner" role="img" aria-label="Soft grey halftone dot pattern fading from the top-left corner"></div>

  <svg class="frame-shapes" width="1200" height="323" viewBox="0 0 1200 323" aria-hidden="true">
    <polygon points="732,0 1200,0 1200,54 772,54" fill="var(--gold)"/>
    <polygon points="0,292 606,292 610,297 0,297" fill="var(--gold)"/>
    <polygon points="0,297 610,297 636,323 0,323" fill="var(--ink)"/>
    <rect x="640" y="317" width="560" height="2" fill="var(--rule-grey)"/>
  </svg>

  <p class="company-tagline">The KALV Electric Way</p>

  <div class="company-mark">
    <span class="company-mark-square"></span>
    <span>KALV Electric</span>
  </div>

  <div class="identity">
    <h1 class="person-name">Jordan Hale</h1>
    <p class="person-title">Marketing Manager</p>
  </div>

  <div class="divider"></div>

  <ul class="contacts">
    <li class="contact">
      <svg class="contact-icon" viewBox="0 0 34 34" aria-hidden="true">
        <circle cx="17" cy="17" r="16" fill="var(--ink)"/>
        <rect x="9" y="11" width="16" height="12" rx="1.5" fill="var(--gold)"/>
        <polyline points="9.5,12 17,18 24.5,12" fill="none" stroke="var(--ink)" stroke-width="1.6"/>
      </svg>
      <span>name@thecompany.com</span>
    </li>
    <li class="contact">
      <svg class="contact-icon" viewBox="0 0 34 34" aria-hidden="true">
        <circle cx="17" cy="17" r="16" fill="var(--ink)"/>
        <g fill="none" stroke="var(--gold)" stroke-width="1.6">
          <circle cx="17" cy="17" r="8"/>
          <ellipse cx="17" cy="17" rx="3.5" ry="8"/>
          <line x1="9" y1="17" x2="25" y2="17"/>
          <line x1="10.5" y1="13" x2="23.5" y2="13"/>
          <line x1="10.5" y1="21" x2="23.5" y2="21"/>
        </g>
      </svg>
      <span>yourwebaddress.com</span>
    </li>
    <li class="contact">
      <svg class="contact-icon" viewBox="0 0 34 34" aria-hidden="true">
        <circle cx="17" cy="17" r="16" fill="var(--ink)"/>
        <path d="M11.5 9.5 l3.5 -0.5 l2 4.5 l-2.2 1.6 c1 2.2 2.6 3.8 4.8 4.8 l1.6 -2.2 l4.5 2 l-0.5 3.5 c-0.2 1 -1 1.6 -2 1.6 c-7 -0.4 -12.6 -6 -13 -13 c0 -1 0.6 -1.8 1.3 -2.3 z" fill="var(--gold)"/>
      </svg>
      <span class="phone-lines">
        123 456 7890 <span class="phone-label">(Home)</span><br>
        123 456 7890 <span class="phone-label">(Office)</span>
      </span>
    </li>
  </ul>

  <nav class="social-links" aria-label="Social profiles">
    <span>Pagebook</span>
    <span>Linkora</span>
    <span>Postly</span>
  </nav>
</div>
</body>
</html>
```